Webdesign für psychotherapeutische Praxis
Zielgruppe
Psychotherapeutische Praxis für erwachsene Patienten mit psychischen Erkrankungen.
Die Website soll eine solide, vertrauensvolle Information über das therapeutische Angebot bieten sowie alle Informationen zur Erstkontaktaufnahme erhalten.
Aufgabenstellung
Logo füge ich bei. Die Farben, das Design, die Schrift sollen dem Logo entsprechen (Grau, Violett-Pink Töne, moderne Schrift).

```html
<!DOCTYPE html>
<html lang="de">
<head>
<meta charset="utf-8">
<title>Psychotherapeutische Praxis – Dipl.-Psych. Carla Wendrik</title>
<link href="https://fonts.googleapis.com/css2?family=Fira+Sans:wght@300;400;500;700&family=Ubuntu:wght@300;400;500;700&display=swap" rel="stylesheet">
<style>
:root{
  --violet:#6557a4;
  --violet-light:#7a6cb4;
  --pink:#c05aa6;
  --pink-soft:#d07bb8;
  --grey:#555;
  --grey-light:#777;
  --white:#fff;
}
*{margin:0;padding:0;box-sizing:border-box}
html,body{width:714px;height:1200px;overflow:hidden}
body{position:relative;font-family:"Fira Sans",sans-serif;color:var(--grey);background:var(--white)}
.abs{position:absolute}

/* top bar */
.topbar{left:0;top:0;width:714px;height:17px;background:linear-gradient(180deg,#8a5db0,#b862a8);color:#fff;font-size:4.6px;font-family:Arial,sans-serif}
.topbar span{position:absolute;top:5.5px;display:flex;align-items:center;gap:3px}
.topbar svg{width:5px;height:5px}

/* header */
.header{left:0;top:17px;width:714px;height:37px;background:#fff}
.brand{left:130px;top:12px;display:flex;align-items:center;gap:6px}
.brand-dot{width:14px;height:14px;border-radius:50%;background:var(--violet);margin-right:6px}
.brand-text{font-family:"Ubuntu",sans-serif;color:#4b3f6e;line-height:1.15}
.brand-text .l1{font-size:6.2px}
.brand-text .l2{font-size:5.5px;font-weight:500}
.brand-text .l3{font-size:3.2px}
.header .sep{top:0;width:1px;height:37px;background:#eee}
.nav{right:158px;top:15px;display:flex;gap:9.5px;font-size:6.2px;font-family:"Ubuntu",sans-serif;font-weight:300;color:#555}
.nav .active{color:var(--pink)}
.burger{left:576px;top:16px;width:8px}
.burger i{display:block;height:0.9px;background:#444;margin-bottom:1.3px}

/* hero */
.hero{left:0;top:54px;width:714px;height:253px;background:radial-gradient(ellipse at 30% 20%,#e8e4c8 0%,#e9cc58 35%,#dcae26 70%,#c98f1a 100%)}
.hero-frame{left:138px;top:95px;width:438px;height:171px;border:3.5px solid rgba(255,255,255,.8)}
.hero-frame::after{content:"";position:absolute;inset:3px;border:1.5px solid rgba(255,255,255,.85)}
.hero-title{left:138px;top:161px;width:382px;text-align:right;font-family:"Ubuntu",sans-serif;font-weight:700;font-size:34px;color:#fff;letter-spacing:-.5px}
.hero-sub{left:300px;top:199px;width:220px;text-align:right;font-size:6.7px;font-weight:300;line-height:1.22;color:#6a5a2a}

/* praxis */
.praxis{left:0;top:307px;width:714px;height:271px}
.praxis svg{position:absolute;left:0;top:0}
.section-title{font-family:"Ubuntu",sans-serif;font-weight:300;display:flex;align-items:center;gap:8px}
.section-title::before{content:"";display:block;width:15px;height:1.3px;background:var(--pink)}
.praxis-title{left:134px;top:350px;font-size:14px;color:#fff}
.praxis-text{left:134px;top:374px;width:210px;font-size:6.1px;line-height:1.28;color:#fff;font-weight:300}
.praxis-text p{margin-bottom:7px}
.btn{display:flex;align-items:center;gap:6px;background:var(--pink);color:#fff;border-radius:10px;font-size:5.7px;letter-spacing:.3px;padding:0 8px;height:18px;font-weight:400}
.btn svg{width:11px;height:4px}
.btn-praxis{left:134px;top:451px;width:117px}
.hours-title{left:134px;top:484px;display:flex;align-items:center;gap:5px;font-size:7.4px;color:#fff;font-weight:500}
.hours-title svg{width:10px;height:10px}
.hours{top:501px;font-size:6.1px;color:#fff;font-weight:300;line-height:1.3;display:grid;grid-template-columns:42px auto}
.photo{background:linear-gradient(135deg,#ddd,#9a9a9a)}
.photo-entry{left:486px;top:357px;width:101px;height:106px;background:linear-gradient(160deg,#f3f2ee 0%,#c9c7c0 45%,#3e3e3e 75%,#6a6a64 100%)}
.photo-reception{left:357px;top:398px;width:150px;height:98px;background:linear-gradient(100deg,#5c8a4a 0%,#e9e8e4 25%,#f4f2ee 55%,#c79a58 85%,#e8e6e2 100%)}

/* about */
.about-title{left:130px;top:656px;font-size:14.5px;color:#555}
.about-text{left:130px;top:681px;width:145px;font-size:6.1px;line-height:1.28;font-weight:300;color:#666}
.about-text p{margin-bottom:7px}
.about-text b{font-weight:500;color:#444}
.btn-about{left:130px;top:781px;width:65px}
.card{background:#fff;box-shadow:0 2px 10px rgba(80,60,120,.12);padding:15px 15px}
.card h3{font-family:"Ubuntu",sans-serif;font-weight:400;font-size:7.6px;color:var(--violet);margin:10px 0 7px}
.card p{font-size:5.8px;line-height:1.3;font-weight:300;color:#666;margin-bottom:7px}
.card a{font-size:5.2px;font-weight:500;color:var(--pink);text-decoration:none;border-bottom:1px solid var(--pink)}
.card svg{width:26px;height:26px}
.card-offer{left:291px;top:632px;width:131px;height:133px}
.card-flow{left:445px;top:609px;width:131px;height:134px}

/* contact */
.contact-bg{left:0;top:843px;width:714px;height:196px;background:linear-gradient(180deg,#f1eef6 0%,#e6e1ef 50%,#d9cfe3 100%)}
.contact-title{left:0;top:882px;width:714px;text-align:center;font-family:"Ubuntu",sans-serif;font-weight:300;font-size:14px;color:#555}
.contact-line{left:348px;top:901px;width:18px;height:1.4px;background:var(--violet)}
.contact-text{left:220px;top:931px;width:274px;text-align:center;font-size:7.5px;font-weight:300;color:#555;line-height:1.22}
.btn-contact{left:307px;top:974px;width:99px;justify-content:center}

/* footer */
.footer{left:0;top:1039px;width:714px;height:161px;background:linear-gradient(180deg,var(--violet) 0%,var(--violet) 78%,#a45fa8 100%)}
.footer-box{left:130px;top:1036px;width:297px;height:104px;background:var(--violet-light);border-top:3px solid var(--pink);padding:24px 15px 0}
.footer-box .brand-text{color:#fff}
.footer-box .fbrand{display:flex;align-items:center}
.footer-box .brand-dot{width:12px;height:12px;background:var(--pink-soft)}
.footer-box p{font-size:5.3px;line-height:1.55;color:#fff;font-weight:300;margin-top:11px}
.flinks{top:1060px;width:63px;font-size:5.4px;color:#fff;font-weight:300}
.flinks li{list-style:none;border-bottom:.7px solid rgba(255,255,255,.35);padding:3px 0 3.2px}
.flinks li:last-child{border-bottom:none}
.copy{left:130px;top:1177px;font-size:5px;color:#fff}
.totop{left:567px;top:1172px;width:17px;height:17px;border:1px solid #fff;display:flex;align-items:center;justify-content:center}
</style>
</head>
<body>

<div class="abs topbar">
  <span style="left:132px"><svg viewBox="0 0 10 10"><path d="M2 1l2 2-1 1.5c.6 1.2 1.4 2 2.5 2.5L7 6l2 2-1.5 1.5C4.5 9 1 5.5.5 2.5z" fill="#fff"/></svg>0123 987 6540</span>
  <span style="left:184px"><svg viewBox="0 0 10 10"><rect x=".8" y="2" width="8.4" height="6" fill="none" stroke="#fff" stroke-width="1"/><path d="M1 2.5l4 3 4-3" fill="none" stroke="#fff" stroke-width="1"/></svg>info@wendrikhauslo.de</span>
  <span style="left:504px"><svg viewBox="0 0 10 10"><rect x="2" y="2" width="6" height="6" fill="none" stroke="#fff" stroke-width="1"/></svg>Datenschutzerklärung nach DSGVO</span>
</div>

<header class="abs header">
  <div class="abs brand">
    <div class="brand-dot"></div>
    <div class="brand-text">
      <div class="l1">Psychotherapeutische Praxis</div>
      <div class="l2">DIPL.-PSYCH. CARLA WENDRIK</div>
      <div class="l3">Psychologische Psychotherapeutin (VT)</div>
    </div>
  </div>
  <div class="abs sep" style="left:268px"></div>
  <nav class="abs nav">
    <span class="active">Startseite</span><span>Therapieangebot</span><span>Therapieablauf</span><span>Über mich</span><span>Kontakt</span>
  </nav>
  <div class="abs sep" style="left:563px"></div>
  <div class="abs burger"><i></i><i></i><i></i></div>
</header>

<section class="abs hero" role="img" aria-label="Foto: Frau mit ausgebreiteten Armen in einem sonnigen Kornfeld"></section>
<div class="abs hero-frame"></div>
<h1 class="abs hero-title">Herzlich Willkommen</h1>
<p class="abs hero-sub">Muster Willkommenstext Lorem ipsum dolor sit amet consetetur sadipscing elitr, sed diam nonumy eirmod tempor invidunt ilabore et dolore magna aliquyam erat, sed diam voluptua!</p>

<section class="abs praxis">
  <svg width="714" height="271" viewBox="0 0 714 271"><polygon points="0,0 714,0 714,248 0,271" fill="#6557a4"/></svg>
</section>
<h2 class="abs section-title praxis-title">Praxis</h2>
<div class="abs praxis-text">
  <p>Herzlich Willkommen bei <b style="font-weight:500">Psychotherapeutische Praxis – Carla Wendrik</b></p>
  <p>Wir sind gern für Sie da und sehr bemüht, Ihnen zeitnah einen Therapieplatz anzubieten.<br>Hier finden Sie Informationen über unsere Praxis, Therapieangebot und Therapieablauf. Wir möchten Sie einladen, sich hier einen ersten Eindruck über unser Therapieangebot zu verschaffen oder gern direkt mit uns Kontakt aufzunehmen.</p>
</div>
<div class="abs btn btn-praxis">JETZT KONTAKT AUFNEHMEN <svg viewBox="0 0 22 8"><path d="M0 4h20M17 1l3 3-3 3" fill="none" stroke="#fff" stroke-width="1"/></svg></div>
<div class="abs hours-title"><svg viewBox="0 0 20 20"><circle cx="10" cy="10" r="8.5" fill="none" stroke="#c05aa6" stroke-width="1.5"/><path d="M10 5v5l3 2" fill="none" stroke="#c05aa6" stroke-width="1.5"/></svg>Öffnungszeiten:</div>
<div class="abs hours" style="left:134px"><span>Montag:</span><span>09:00–20:00</span><span>Dienstag:</span><span>09:00–20:00</span><span>Mittwoch:</span><span>09:00–20:00</span><span>Donnerstag:</span><span>09:00–20:00</span></div>
<div class="abs hours" style="left:241px;grid-template-columns:37px auto"><span>Freitag:</span><span>09:00–20:00</span><span>Samstag:</span><span>10:00–14:00</span><span>Sonntag:</span><span>&nbsp;Geschlossen</span></div>
<div class="abs photo-entry" role="img" aria-label="Foto: Eingangsportal des Praxisgebäudes"></div>
<div class="abs photo-reception" role="img" aria-label="Foto: Empfangsbereich der Praxis"></div>

<h2 class="abs section-title about-title">Carla Wendrik</h2>
<div class="abs about-text">
  <p>Muster Text dolor sit amet, consetetur sadipscing elitr, sed diam nonumy eirmod tempor invidunt ut labore et dolore magna aliquyam erat, sed diam voluptua estil vero eos et <b>accusam et justo duo dolores</b> et ea rebum. Stet clita kasd gubergren no sea takimata sanctus est Lorem ipsum dolor sit amet. Lorem ipsum dolor sit amet, consetetur sadipscing elitr.</p>
  <p>Sed diam nonumy eirmod tempor invidunt ut labore et dolore et magna aliquyam erat, sed diam voluptua. At vero eos et accusam.</p>
</div>
<div class="abs btn btn-about">ÜBER MICH <svg viewBox="0 0 22 8"><path d="M0 4h20M17 1l3 3-3 3" fill="none" stroke="#fff" stroke-width="1"/></svg></div>

<article class="abs card card-offer">
  <svg viewBox="0 0 30 30"><path d="M8 26v-5c-3-2-4-5-3-9 1-5 6-8 11-7 4 1 6 4 6 8l2 4h-2v3c0 1-1 2-3 2h-2v4" fill="none" stroke="#6557a4" stroke-width="1"/><circle cx="13" cy="13" r="5" fill="none" stroke="#c05aa6" stroke-width=".9"/><circle cx="13" cy="13" r="3" fill="none" stroke="#c05aa6" stroke-width=".9"/><circle cx="13" cy="13" r="1" fill="#c05aa6"/><path d="M20 4h7M25 2l2 2-2 2" fill="none" stroke="#c05aa6" stroke-width=".9"/></svg>
  <h3>Therapieangebot</h3>
  <p>Lorem ipsum dolor sit amet, consectetur adipiscing elit. Ut elit tellus, luctus nec ullamcorper mattis, pulvinar dapibus leo.</p>
  <a>MEHR ERFAHREN</a>
</article>
<article class="abs card card-flow">
  <svg viewBox="0 0 30 30"><path d="M3 3h20a4 4 0 0 1 0 8H7a4 4 0 0 0 0 8h17" fill="none" stroke="#6557a4" stroke-width="1"/><circle cx="3" cy="3" r="1.5" fill="none" stroke="#c05aa6"/><circle cx="13" cy="11" r="1.2" fill="#c05aa6"/><circle cx="25" cy="20" r="1.5" fill="none" stroke="#c05aa6"/><path d="M20 12v5M20 12h3v2h-3" fill="none" stroke="#c05aa6" stroke-width=".8"/></svg>
  <h3>Therapieablauf</h3>
  <p>Lorem ipsum dolor sit amet, consectetur adipiscing elit. Ut elit tellus, luctus nec ullamcorper mattis, pulvinar dapibus leo.</p>
  <a>MEHR ERFAHREN</a>
</article>

<section class="abs contact-bg" role="img" aria-label="Verblasstes Foto einer Stadtsilhouette bei Nacht"></section>
<h2 class="abs contact-title">Kontakt</h2>
<div class="abs contact-line"></div>
<p class="abs contact-text">Bei Fragen stehen wir Ihnen gerne zur Verfügung. Am besten erreichen Sie uns via E-Mail oder über das Kontaktformular.</p>
<div class="abs btn btn-contact">KONTAKT AUFNEHMEN <svg viewBox="0 0 22 8"><path d="M0 4h20M17 1l3 3-3 3" fill="none" stroke="#fff" stroke-width="1"/></svg></div>

<footer class="abs footer"></footer>
<div class="abs footer-box">
  <div class="fbrand">
    <div class="brand-dot"></div>
    <div class="brand-text">
      <div class="l1" style="font-size:5.4px">Psychotherapeutische Praxis</div>
      <div class="l2" style="font-size:4.8px">DIPL.-PSYCH. CARLA WENDRIK</div>
      <div class="l3" style="font-size:2.8px">Psychologische Psychotherapeutin (VT)</div>
    </div>
  </div>
  <p>Muster kurze über Praxis Text Etiam magna arcu, ullamcorper ut pulvinar et, ornare sit amet ligula. Aliquam vitae bibendum lorem. Cras id dui lectus. Pellentesque nec felis tristique urna lacinia sollicitudin ac ac ex. Maecenas mattis faucibus condimentum.</p>
</div>
<ul class="abs flinks" style="left:442px"><li>Startseite</li><li>Therapieangebot</li><li>Therapieablauf</li><li>Über mich</li><li>Kontakt</li></ul>
<ul class="abs flinks" style="left:520px"><li>Impressum</li><li>Datenschutz</li><li>Cookie-Richtlinie</li><li>Datenschutzerklärung nach DSGVO</li></ul>
<div class="abs copy">© 2020 Psychotherapeutische Praxis - DIPL.-PSYCH. CARLA WENDRIK. Alle Rechte vorbehalten.</div>
<div class="abs totop"><svg width="7" height="5" viewBox="0 0 7 5"><path d="M1 4l2.5-2.5L6 4" fill="none" stroke="#fff" stroke-width="1"/></svg></div>

</body>
</html>
```